Corvale Homes

To produce a business card design for our newly established house building and development company, We have had a logo design done please see attached, our slogan is "Crafting the place you call home"
Contact Information for Business Card
Adress on card needs to Read - 58 Elmsworth Lane, Thornbury Vale, Eastmoorshire EV16 4QT. Director name Dean Vascotti
Requirements
Must have
- Web adress is www.corvale-homes.co.uk
- Email address is info@corvale-homes.co.uk
- phone number 07700 900417

```html
<!DOCTYPE html>
<html lang="en">
<head>
<meta charset="utf-8">
<title>Corvale Homes – Business Card</title>
<link rel="stylesheet" href="https://fonts.googleapis.com/css2?family=Montserrat:wght@300;400;600;700&display=swap">
<style>
  :root {
    --bg: #d9d9d9;
    --card: #f1f1f1;
    --dark: #363636;
    --green: #7cbd3b;
    --grey: #9b9b9b;
    --text-light: #f4f4f4;
    --shadow: rgba(0,0,0,0.18);
  }
  * { box-sizing: border-box; margin: 0; padding: 0; }
  html, body { width: 1200px; height: 1000px; overflow: hidden; }
  body {
    background: var(--bg);
    font-family: "Montserrat", sans-serif;
    position: relative;
  }
  .card {
    position: absolute;
    left: 250px;
    width: 700px;
    height: 400px;
    background: var(--card);
    box-shadow: 0 6px 18px var(--shadow);
    overflow: hidden;
  }
  .card--front { top: 80px; }
  .card--back { top: 520px; }

  /* brand lockup */
  .brand {
    position: absolute;
    text-align: center;
  }
  .brand__name {
    display: flex;
    align-items: center;
    justify-content: center;
    gap: 12px;
    color: var(--green);
    font-weight: 700;
    font-size: 34px;
    letter-spacing: 1px;
    text-transform: uppercase;
    white-space: nowrap;
  }
  .brand__dot {
    width: 14px; height: 14px;
    border-radius: 50%;
    background: var(--green);
    flex: none;
  }
  .brand__tagline {
    margin-top: 10px;
    font-size: 8px;
    font-weight: 600;
    letter-spacing: 3.5px;
    text-transform: uppercase;
    color: var(--green);
    white-space: nowrap;
  }

  /* front */
  .card--front .brand { left: 20px; top: 150px; width: 300px; }
  .card--front .brand__name { font-size: 27px; }
  .corner-bars { position: absolute; left: 0; top: 0; }
  .info-panel {
    position: absolute;
    left: 330px; top: 0;
    width: 370px; height: 400px;
    background: var(--dark);
    color: var(--text-light);
    padding: 62px 0 0 54px;
  }
  .info-panel__tab {
    position: absolute;
    left: -12px; top: 92px;
    width: 36px; height: 48px;
    background: var(--green);
  }
  .person__name { font-size: 27px; font-weight: 300; white-space: nowrap; }
  .person__name span { color: var(--green); }
  .person__role { font-size: 13px; font-weight: 600; margin-top: 4px; margin-left: 20px; }
  .contacts { position: absolute; left: 70px; top: 150px; }
  .contacts svg { position: absolute; left: 0; top: 0; }
  .contact {
    position: absolute;
    left: 50px;
    font-size: 13px;
    font-weight: 300;
    line-height: 1.35;
    white-space: nowrap;
  }

  /* back */
  .card--back .brand { left: 0; top: 125px; width: 700px; }
  .card--back .brand__name { font-size: 40px; }
  .web-band {
    position: absolute;
    left: 0; bottom: 0;
    width: 700px; height: 56px;
    background: var(--green);
    color: #ffffff;
    font-size: 17px;
    font-weight: 600;
    letter-spacing: 1px;
    display: flex;
    align-items: center;
    justify-content: center;
  }
</style>
</head>
<body>

<section class="card card--front" aria-label="Business card front">
  <svg class="corner-bars" width="120" height="400" viewBox="0 0 120 400" aria-hidden="true">
    <polygon points="40,225 85,240 85,300 40,300" fill="var(--green)"/>
    <polygon points="40,300 85,300 95,400 40,400" fill="var(--grey)"/>
  </svg>

  <div class="brand">
    <div class="brand__name"><span class="brand__dot"></span>Corvale Homes</div>
    <div class="brand__tagline">Crafting the place you call home</div>
  </div>

  <div class="info-panel">
    <div class="info-panel__tab"></div>
    <h1 class="person__name">Dean <span>Vascotti</span></h1>
    <p class="person__role">Director</p>

    <div class="contacts">
      <svg width="46" height="170" viewBox="0 0 46 170" aria-hidden="true">
        <line x1="20" y1="20" x2="20" y2="140" stroke="var(--green)" stroke-width="1.5"/>
        <polygon points="20,4 34,12 34,28 20,36 6,28 6,12" fill="var(--dark)" stroke="var(--green)" stroke-width="2"/>
        <rect x="15" y="12" width="10" height="16" rx="1.5" fill="none" stroke="#fff" stroke-width="1.5"/>
        <polygon points="20,62 34,70 34,86 20,94 6,86 6,70" fill="var(--dark)" stroke="var(--green)" stroke-width="2"/>
        <rect x="13" y="72" width="14" height="10" rx="1" fill="none" stroke="#fff" stroke-width="1.5"/>
        <polyline points="13,72 20,78 27,72" fill="none" stroke="#fff" stroke-width="1.2"/>
        <polygon points="20,122 34,130 34,146 20,154 6,146 6,130" fill="var(--green)"/>
        <path d="M20 147 C15 141 14 138 14 135 A6 6 0 0 1 26 135 C26 138 25 141 20 147 Z" fill="#fff"/>
        <circle cx="20" cy="135" r="2" fill="var(--green)"/>
      </svg>
      <p class="contact" style="top:10px">07700 900417</p>
      <p class="contact" style="top:69px">info@corvale-homes.co.uk</p>
      <p class="contact" style="top:121px">58 Elmsworth Lane, Thornbury Vale,<br>Eastmoorshire EV16 4QT</p>
    </div>
  </div>
</section>

<section class="card card--back" aria-label="Business card back">
  <div class="brand">
    <div class="brand__name"><span class="brand__dot"></span>Corvale Homes</div>
    <div class="brand__tagline">Crafting the place you call home</div>
  </div>
  <div class="web-band">www.corvale-homes.co.uk</div>
</section>

</body>
</html>
```